Poster design for a company operating care homes in the UK showcasing our core values

We need a poster to display in our care homes showcasing our new core values:

Purpose
We are driven by a clear understanding of why we do what we do: to enrich lives, honour legacies and make a meaningful difference every day, for our residents, their families, our colleagues and our community.

Excellence
We hold ourselves to the highest standards, delivering exceptional care and creating an environment where both residents and staff can thrive.

Openness
We build trust through honest, respectful communication, welcoming feedback, sharing ideas, and embracing change as a path to continuous growth.

Passion
We are passionate about delivering exceptional care. We take pride in what we do and in making a real difference in people’s lives.

Learning
We are committed to personal and professional growth; empowering each other through ongoing development, reflection, and shared knowledge.

Empathy
We actively listen and seek to understand before being understood, recognising the unique stories, feelings, and needs of others.

I have attached a small graphic that we would like you try to incorporate, in addition to our company logo. Please theme the rest of the poster around our company colours.

```html
<!DOCTYPE html>
<html lang="en">
<head>
<meta charset="utf-8">
<title>Halverton – Our Values</title>
<link href="https://fonts.googleapis.com/css2?family=Amatic+SC:wght@700&family=Nunito+Sans:wght@400;600;800&family=Luckiest+Guy&display=swap" rel="stylesheet">
<style>
  :root {
    --navy: #2f4460;
    --peach: #d4875e;
    --peach-line: #e2a27c;
    --bg-top: #f0e3da;
    --bg-bottom: #dc9f7b;
    --cell-fill: rgba(247, 233, 224, 0.72);
    --page: #e9e7e4;
  }
  * { box-sizing: border-box; margin: 0; padding: 0; }
  html, body { width: 1093px; height: 1200px; overflow: hidden; background: var(--page); }
  .poster {
    position: absolute; left: 140px; top: 20px; width: 812px; height: 1160px;
    background: linear-gradient(180deg, var(--bg-top) 0%, #ecd2c1 45%, var(--bg-bottom) 100%);
    overflow: hidden;
    font-family: "Nunito Sans", sans-serif;
    color: var(--navy);
  }
  .acronym-cell {
    position: absolute; width: 100px; height: 100px;
    display: flex; align-items: center; justify-content: center;
    font-family: "Luckiest Guy", sans-serif; font-size: 8.5px; letter-spacing: .2px;
    white-space: nowrap;
  }
  .acronym-cell svg { position: absolute; inset: 0; }
  .acronym-cell span { position: relative; display: flex; align-items: baseline; }
  .acronym-cell b { font-size: 22px; font-weight: 400; line-height: 1; }
  .acronym-cell.light svg polygon { fill: var(--peach); stroke: var(--peach); }
  .acronym-cell.light span { color: var(--navy); }
  .acronym-cell.dark svg polygon { fill: var(--navy); stroke: var(--navy); }
  .acronym-cell.dark span { color: var(--peach); }

  .value {
    position: absolute; width: 235px; height: 260px;
    display: flex; flex-direction: column; align-items: center; justify-content: center;
    text-align: center; padding: 0 26px;
  }
  .value > svg.cell { position: absolute; inset: 0; z-index: 0; }
  .value > * { position: relative; z-index: 1; }
  .value .icon { width: 46px; height: 46px; stroke: var(--navy); fill: none; stroke-width: 2.6; stroke-linecap: round; stroke-linejoin: round; }
  .value h2 {
    font-family: "Amatic SC", sans-serif; font-weight: 700; font-size: 50px; line-height: .95; letter-spacing: 0;
    margin: 2px 0 4px; white-space: nowrap;
  }
  .value p { font-size: 11px; line-height: 1.25; }

  .care-photo {
    position: absolute; left: 230px; top: 450px; width: 330px; height: 290px;
    background: radial-gradient(ellipse at 50% 50%, #b59a86 0%, #c9a78f 40%, rgba(224,180,152,0.6) 62%, rgba(224,180,152,0) 72%);
  }

  .brand { position: absolute; left: 0; right: 0; top: 1040px; text-align: center; }
  .brand-name {
    display: inline-flex; align-items: center; gap: 18px;
    font-family: "Nunito Sans", sans-serif; font-weight: 800; font-size: 72px; letter-spacing: 2px; color: var(--navy); line-height: 1;
  }
  .brand-name i { width: 48px; height: 48px; background: var(--navy); display: inline-block; }
</style>
</head>
<body>
<main class="poster">

  <div class="acronym-cell light" style="left:145px;top:73px"><svg viewBox="0 0 100 100"><polygon points="50,6 90,28 90,72 50,94 10,72 10,28" stroke-width="10" stroke-linejoin="round"/></svg><span><b>P</b>URPOSE</span></div>
  <div class="acronym-cell dark" style="left:227px;top:42px"><svg viewBox="0 0 100 100"><polygon points="50,6 90,28 90,72 50,94 10,72 10,28" stroke-width="10" stroke-linejoin="round"/></svg><span><b>E</b>XCELLENCE</span></div>
  <div class="acronym-cell light" style="left:308px;top:73px"><svg viewBox="0 0 100 100"><polygon points="50,6 90,28 90,72 50,94 10,72 10,28" stroke-width="10" stroke-linejoin="round"/></svg><span><b>O</b>PENNESS</span></div>
  <div class="acronym-cell dark" style="left:390px;top:42px"><svg viewBox="0 0 100 100"><polygon points="50,6 90,28 90,72 50,94 10,72 10,28" stroke-width="10" stroke-linejoin="round"/></svg><span><b>P</b>ASSION</span></div>
  <div class="acronym-cell light" style="left:473px;top:73px"><svg viewBox="0 0 100 100"><polygon points="50,6 90,28 90,72 50,94 10,72 10,28" stroke-width="10" stroke-linejoin="round"/></svg><span><b>L</b>EARNING</span></div>
  <div class="acronym-cell dark" style="left:555px;top:42px"><svg viewBox="0 0 100 100"><polygon points="50,6 90,28 90,72 50,94 10,72 10,28" stroke-width="10" stroke-linejoin="round"/></svg><span><b>E</b>MPATHY</span></div>

  <div class="care-photo" role="img" aria-label="Photo of a carer sharing a meal and conversation with an elderly resident"></div>

  <section class="value" style="left:277px;top:199px">
    <svg class="cell" viewBox="0 0 235 260"><polygon points="117.5,5 230,68 230,192 117.5,255 5,192 5,68" fill="var(--cell-fill)" stroke="var(--peach-line)" stroke-width="6" stroke-linejoin="round"/></svg>
    <svg class="icon" viewBox="0 0 48 48"><circle cx="22" cy="26" r="17"/><circle cx="22" cy="26" r="10"/><circle cx="22" cy="26" r="3"/><path d="M22 26 L40 8 M36 6 L40 8 L42 12"/></svg>
    <h2>Purpose</h2>
    <p>We are driven by a clear understanding of why we do what we do: to enrich lives, honour legacies and make a meaningful difference every day, for our residents, their families, our colleagues and our community.</p>
  </section>

  <section class="value" style="left:37px;top:332px">
    <svg class="cell" viewBox="0 0 235 260"><polygon points="117.5,5 230,68 230,192 117.5,255 5,192 5,68" fill="var(--cell-fill)" stroke="var(--peach-line)" stroke-width="6" stroke-linejoin="round"/></svg>
    <svg class="icon" viewBox="0 0 48 48"><circle cx="24" cy="20" r="15"/><circle cx="24" cy="20" r="10"/><path d="M24 14 l2 4.5 4.5.5-3.4 3 1 4.6-4.1-2.4-4.1 2.4 1-4.6-3.4-3 4.5-.5z"/><path d="M16 33 L12 45 M32 33 L36 45"/></svg>
    <h2>Excellence</h2>
    <p>We hold ourselves to the highest standards, delivering exceptional care and creating an environment where both residents and staff can thrive.</p>
  </section>

  <section class="value" style="left:522px;top:332px">
    <svg class="cell" viewBox="0 0 235 260"><polygon points="117.5,5 230,68 230,192 117.5,255 5,192 5,68" fill="var(--cell-fill)" stroke="var(--peach-line)" stroke-width="6" stroke-linejoin="round"/></svg>
    <svg class="icon" viewBox="0 0 60 48" style="width:66px"><path d="M20 8 c10 0 16 5 16 11 s-6 11-16 11 c-2 0-3 0-5-1 l-7 5 2-7 c-4-2-6-5-6-8 0-6 6-11 16-11z"/><path d="M38 6 c10 0 17 5 17 11 0 3-2 6-6 8 l2 7-7-5 c-2 1-4 1-6 1"/></svg>
    <h2>Openness</h2>
    <p>We build trust through honest, respectful communication, welcoming feedback, sharing ideas, and embracing change as a path to continuous growth.</p>
  </section>

  <section class="value" style="left:38px;top:602px">
    <svg class="cell" viewBox="0 0 235 260"><polygon points="117.5,5 230,68 230,192 117.5,255 5,192 5,68" fill="var(--cell-fill)" stroke="var(--peach-line)" stroke-width="6" stroke-linejoin="round"/></svg>
    <svg class="icon" viewBox="0 0 48 48"><path d="M24 10 c-8 0-13 6-13 12 0 5 3 8 6 11 v4 h14 v-4 c3-3 6-6 6-11 0-6-5-12-13-12z"/><path d="M19 42 h10"/><path d="M24 30 l-6-6 c-2-2 0-6 3-5 2 0 3 2 3 2 s1-2 3-2 c3-1 5 3 3 5z"/><path d="M24 2 v3 M8 8 l2 2 M40 8 l-2 2 M2 22 h3 M43 22 h3"/></svg>
    <h2>Passion</h2>
    <p>We are passionate about delivering exceptional care. We take pride in what we do and in making a real difference in people’s lives.</p>
  </section>

  <section class="value" style="left:524px;top:602px">
    <svg class="cell" viewBox="0 0 235 260"><polygon points="117.5,5 230,68 230,192 117.5,255 5,192 5,68" fill="var(--cell-fill)" stroke="var(--peach-line)" stroke-width="6" stroke-linejoin="round"/></svg>
    <svg class="icon" viewBox="0 0 48 48"><path d="M6 18 h14 c2 0 4 2 4 4 c0-2 2-4 4-4 h14 v26 h-14 c-2 0-4 1-4 2 c0-1-2-2-4-2 h-14z"/><path d="M24 22 v24"/><path d="M17 14 a7 7 0 0 1 14 0 M24 2 v4 M13 6 l3 3 M35 6 l-3 3"/></svg>
    <h2>Learning</h2>
    <p>We are committed to personal and professional growth; empowering each other through ongoing development, reflection, and shared knowledge.</p>
  </section>

  <section class="value" style="left:285px;top:729px">
    <svg class="cell" viewBox="0 0 235 260"><polygon points="117.5,5 230,68 230,192 117.5,255 5,192 5,68" fill="var(--cell-fill)" stroke="var(--peach-line)" stroke-width="6" stroke-linejoin="round"/></svg>
    <svg class="icon" viewBox="0 0 48 48"><path d="M24 44 L7 27 c-6-6-3-19 7-19 5 0 8 3 10 6 2-3 5-6 10-6 10 0 13 13 7 19z"/><path d="M14 24 l8-6 c2-1 4 0 6 1 l8 8 M18 30 l4 4 M22 27 l5 5 M26 24 l5 5"/></svg>
    <h2>Empathy</h2>
    <p>We actively listen and seek to understand before being understood, recognising the unique stories, feelings, and needs of others.</p>
  </section>

  <footer class="brand">
    <div class="brand-name"><i></i>HALVERTON</div>
  </footer>

</main>
</body>
</html>
```